File Download Website

We are looking for a design for a file download website. Our objective is to allow users to upload/browse/download files. This means we need 3 different pages.
The upload page should allow users to upload a file, we are looking for creative designs, a file box with a browse button next to it is already out there so the design must bring something new.
The browse page should display a users files/folders.
The download page should allow the user to download a file.
We do not require any code, only design. The designer is given complete freedom over the design, you may go about it however you like. This is a test of creativity, whoever this project goes to will definitely be given more work in the near future.
Example of a well designed file download website: cloudvane.net
Target Market(s)
15-30 year old people
Industry/Entity Type
Work
Look and feel
Each slider illustrates characteristics of the customer's brand and the style your logo design should communicate.

```html
<!DOCTYPE html>
<html lang="en">
<head>
<meta charset="utf-8">
<title>Stashbox – My Files</title>
<link href="https://fonts.googleapis.com/css2?family=Arimo:ital,wght@0,400;0,700;1,400&display=swap" rel="stylesheet">
<style>
:root{
  --brand:#0b8dd6;
  --brand-dark:#0872b0;
  --subbar:#456a89;
  --subbar-tab:#1f3c56;
  --text:#555;
  --link:#0a86c6;
  --muted:#777;
  --rule:#cfcfcf;
  --head:#e2e2e2;
  --row-a:#e8f0f5;
  --row-b:#f2f2f2;
  --footer:#efefef;
  --folder:#e8b83a;
  --screen:#6fb7e0;
}
*{box-sizing:border-box;margin:0;padding:0}
html,body{width:1200px;height:953px;overflow:hidden;background:#fff}
body{font-family:"Arimo",Arial,sans-serif;color:var(--text)}
.stage{width:980px;height:778px;transform:scale(1.22449);transform-origin:0 0;position:relative}
.topbar{position:absolute;left:0;top:0;width:980px;height:56px;background:var(--brand)}
.brand{position:absolute;left:26px;top:12px;display:flex;align-items:center;gap:10px;color:#fff;font-size:28px;font-weight:400;letter-spacing:.5px}
.brand-dot{width:26px;height:26px;border-radius:50%;background:#fff}
.search{position:absolute;left:307px;top:10px;width:336px;height:37px;background:#fff;border-radius:6px;overflow:hidden;display:flex}
.search-type{width:95px;background:linear-gradient(#e9e9e9,#cfcfcf);font-size:12px;font-weight:700;color:#555;display:flex;align-items:center;justify-content:center;gap:6px}
.search-field{flex:1;font-size:14px;color:#555;padding-left:10px;display:flex;align-items:center}
.search-icon{position:absolute;right:14px;top:10px}
.usernav{position:absolute;right:14px;top:22px;font-size:12px;color:#fff;display:flex;gap:16px}
.subbar{position:absolute;left:0;top:56px;width:980px;height:38px;background:linear-gradient(var(--subbar),#3a5c79)}
.subbar-tab{position:absolute;left:0;top:0;height:38px;width:136px;background:var(--subbar-tab);clip-path:polygon(0 0,100% 0,91% 100%,0 100%);display:flex;align-items:center;padding-left:30px;gap:8px;color:#fff;font-size:14px}
.sidebar{position:absolute;left:0;top:94px;width:181px;height:349px;border-right:1px solid var(--rule)}
.tree{list-style:none;font-size:12px;color:#666}
.tree li{position:absolute;display:flex;align-items:center;gap:6px}
.tree .root{left:13px;top:17px;font-weight:700;color:#444}
.caret{font-size:8px;color:var(--brand);width:8px}
.toolbar{position:absolute;left:202px;top:109px;display:flex;gap:9px}
.btn{height:34px;border-radius:4px;background:linear-gradient(#1a9be0,var(--brand-dark));color:#fff;font-size:12px;display:flex;align-items:center;gap:6px;padding:0 12px 0 14px;box-shadow:0 1px 0 #05527f}
.files{position:absolute;left:202px;top:157px;width:778px;border-collapse:collapse;font-size:12px}
.files th{height:32px;background:var(--head);text-align:left;font-weight:400;color:#333;border-top:1px solid var(--rule);border-left:1px solid #d2d2d2}
.files th:first-child{border-left:0}
.files td{height:40px;border-bottom:1px solid #fff;border-left:1px solid #fff}
.files td:first-child{border-left:0}
.files tr:nth-child(odd) td{background:var(--row-a)}
.files tr:nth-child(even) td{background:var(--row-b)}
.col-check{width:36px;text-align:center}
.col-name{width:481px;padding-left:9px}
.col-date{padding-left:15px;color:var(--muted)}
.box{display:inline-block;width:12px;height:12px;border:1px solid #bbb;border-radius:2px;background:#fff;vertical-align:middle}
.name{display:flex;align-items:center;gap:8px}
.name a{color:var(--link);font-size:15px;text-decoration:none}
.meta{font-style:italic;color:var(--muted);margin-left:8px}
.statusbar{position:absolute;left:0;top:443px;width:980px;height:46px;background:var(--footer);border-top:2px solid #e2e2e2;display:flex;align-items:center;padding-left:34px;gap:9px;font-size:14px;color:#555}
.statusbar b{color:#555}
</style>
</head>
<body>
<svg width="0" height="0" style="position:absolute">
  <defs>
    <symbol id="folder-screen" viewBox="0 0 30 26">
      <rect x="1" y="3" width="28" height="18" rx="1.5" fill="var(--screen)"/>
      <rect x="3.5" y="5" width="23" height="14" fill="#cfe8f6"/>
      <path d="M6 7h6l2 2h10v9H6z" fill="var(--folder)"/>
      <path d="M5 11h20l-1.5 7H6.5z" fill="#f2cd62"/>
      <rect x="12" y="21" width="6" height="2" fill="var(--screen)"/>
      <rect x="9" y="23" width="12" height="2" rx="1" fill="var(--screen)"/>
    </symbol>
  </defs>
</svg>
<div class="stage">
  <header class="topbar">
    <div class="brand"><span class="brand-dot"></span>Stashbox</div>
    <div class="search">
      <div class="search-type">all types <svg width="10" height="8"><path d="M0 0h10L5 8z" fill="#444"/></svg></div>
      <div class="search-field">Search</div>
      <svg class="search-icon" width="18" height="18" viewBox="0 0 18 18"><circle cx="7" cy="7" r="5.5" fill="none" stroke="#999" stroke-width="2"/><path d="M11 11l6 6" stroke="#999" stroke-width="2.5"/></svg>
    </div>
    <nav class="usernav"><span>My Files</span><span>|</span><span>Settings</span><span>|</span><span>Log Out</span></nav>
  </header>
  <div class="subbar"><div class="subbar-tab"><svg width="22" height="19"><use href="#folder-screen"/></svg>My Files</div></div>
  <aside class="sidebar">
    <ul class="tree">
      <li class="root"><span class="caret">▼</span><svg width="22" height="19"><use href="#folder-screen"/></svg>My Files</li>
      <li style="left:35px;top:48px"><svg width="22" height="19"><use href="#folder-screen"/></svg>Documents</li>
      <li style="left:22px;top:73px"><span class="caret">▶</span><svg width="22" height="19"><use href="#folder-screen"/></svg>Music</li>
      <li style="left:22px;top:98px"><span class="caret">▶</span><svg width="22" height="19"><use href="#folder-screen"/></svg>Photos</li>
      <li style="left:22px;top:123px"><span class="caret">▶</span><svg width="22" height="19"><use href="#folder-screen"/></svg>Videos</li>
    </ul>
  </aside>
  <div class="toolbar">
    <div class="btn"><svg width="18" height="18" viewBox="0 0 18 18"><path d="M2 9l7-7 7 7M2 16l7-7 7 7" fill="none" stroke="#fff" stroke-width="3"/></svg>upload file</div>
    <div class="btn"><svg width="22" height="18" viewBox="0 0 22 18"><path d="M1 2h7l2 2h10v13H1z" fill="#fff"/><path d="M11 7v8M7 11h8" stroke="var(--brand-dark)" stroke-width="2.5"/></svg>create folder</div>
  </div>
  <table class="files">
    <thead><tr><th class="col-check"><span class="box"></span></th><th class="col-name">NAME ▲</th><th class="col-date">MODIFIED</th></tr></thead>
    <tbody>
      <tr><td class="col-check"><span class="box"></span></td><td class="col-name"><div class="name"><svg width="30" height="26"><use href="#folder-screen"/></svg><a href="#">Documents</a><span class="meta">folders: 0, files 0</span></div></td><td class="col-date">2013-06-21 08:43:16</td></tr>
      <tr><td class="col-check"><span class="box"></span></td><td class="col-name"><div class="name"><svg width="30" height="26"><use href="#folder-screen"/></svg><a href="#">Music</a><span class="meta">folders: 0, files 0</span></div></td><td class="col-date">2013-06-21 08:43:16</td></tr>
      <tr><td class="col-check"><span class="box"></span></td><td class="col-name"><div class="name"><svg width="30" height="26"><use href="#folder-screen"/></svg><a href="#">Photos</a><span class="meta">folders: 0, files 0</span></div></td><td class="col-date">2013-06-21 08:43:16</td></tr>
      <tr><td class="col-check"><span class="box"></span></td><td class="col-name"><div class="name"><svg width="30" height="26"><use href="#folder-screen"/></svg><a href="#">Videos</a><span class="meta">folders: 0, files 0</span></div></td><td class="col-date">2013-06-21 08:43:16</td></tr>
    </tbody>
  </table>
  <footer class="statusbar"><svg width="36" height="32"><use href="#folder-screen"/></svg><span><b>My Files</b> has Total of 4 Items</span></footer>
</div>
</body>
</html>
```